Card Design for my dog training business RB Paws Training

Need a business card design for my dog training business with my new logo. Want the card to come off professional yet fun. Want it to be very eye catchy as well. I normally have these at vet clinics, pet stores, and groomers. so need it to look better than my competitors.
Target Market(s)
dog owners
Industry/Entity Type
Dog Training
Contact Information for Business Card
needs logo, my name and info
Font styles to use
Serif
Colors
0255a3
ffffff
ec1f27
000000
333333
fbfbfb
Requirements
Must have
- RB Paws Training
- Lydia Fensworth
- 555 390 2176
- info@rbpawstraining.example
- www.rbpawstraining.example

```html
<!DOCTYPE html>
<html lang="en">
<head>
<meta charset="utf-8">
<title>RB Paws Training — Business Card</title>
<link rel="stylesheet" href="https://fonts.googleapis.com/css2?family=Noto+Serif:wght@400&family=Crimson+Text:ital@1&family=Quattrocento:wght@400&family=Hind:wght@300&display=swap">
<style>
  :root {
    --stage: #cccccc;
    --blue-light: #0090dc;
    --blue-deep: #0255a3;
    --blue-dark: #004e98;
    --red: #ec1f27;
    --charcoal: #3f4346;
    --ink: #333333;
    --paper: #fbfbfb;
    --white: #ffffff;
  }
  * { margin: 0; padding: 0; box-sizing: border-box; }
  html, body { width: 1200px; height: 992px; overflow: hidden; background: var(--stage); }
  .card {
    position: absolute;
    width: 357px;
    height: 591px;
    overflow: hidden;
  }
  .card--front {
    left: 209px; top: 202px;
    background: linear-gradient(160deg, var(--blue-light) 0%, #0073bf 40%, var(--blue-dark) 100%);
  }
  .card--back {
    left: 634px; top: 200px;
    background: var(--paper);
  }
  .brand {
    position: absolute;
    left: 0; right: 0;
    display: flex;
    flex-direction: column;
    align-items: center;
    gap: 18px;
  }
  .brand__mark {
    width: 92px; height: 92px;
    border-radius: 50%;
  }
  .brand__name {
    font-family: "Noto Serif", serif;
    font-weight: 400;
    font-size: 26px;
    letter-spacing: 0.5px;
  }
  .card--front .brand { top: 190px; }
  .card--front .brand__mark { border: 3px solid var(--white); }
  .card--front .brand__name { color: var(--white); }
  .card--back .brand { top: 98px; }
  .card--back .brand__mark { border: 3px solid var(--charcoal); width: 84px; height: 84px; }
  .card--back .brand__name { color: var(--charcoal); font-size: 24px; }
  .tagline {
    position: absolute;
    left: 0; right: 0; top: 532px;
    text-align: center;
    font-family: "Crimson Text", serif;
    font-style: italic;
    font-size: 14px;
    color: var(--white);
  }
  .person {
    position: absolute;
    left: 33px; top: 338px;
  }
  .person__name {
    font-family: "Noto Serif", serif;
    font-weight: 400;
    font-size: 24px;
    color: var(--blue-deep);
    line-height: 1.2;
  }
  .person__role {
    margin-top: 8px;
    font-family: "Quattrocento", serif;
    font-size: 15px;
    color: var(--ink);
  }
  .swoosh { position: absolute; left: 0; top: 0; }
  .contact {
    position: absolute;
    right: 26px; top: 484px;
    list-style: none;
    font-family: "Hind", sans-serif;
    font-weight: 300;
    font-size: 15.5px;
    color: var(--white);
  }
  .contact__item {
    display: flex;
    justify-content: flex-end;
    align-items: center;
    gap: 11px;
    height: 24px;
  }
  .contact__icon { width: 14px; height: 14px; flex: none; }
</style>
</head>
<body>

<section class="card card--front">
  <div class="brand">
    <div class="brand__mark"></div>
    <div class="brand__name">RB Paws Training</div>
  </div>
  <p class="tagline">“Patient training for happy dogs, one pup at a time.”</p>
</section>

<section class="card card--back">
  <div class="brand">
    <div class="brand__mark"></div>
    <div class="brand__name">RB Paws Training</div>
  </div>

  <div class="person">
    <h1 class="person__name">Lydia Fensworth</h1>
    <p class="person__role">Dog Trainer</p>
  </div>

  <svg class="swoosh" width="357" height="591" viewBox="0 0 357 591" aria-hidden="true">
    <path d="M0,490 C90,505 170,470 235,410 C280,372 320,370 357,378 V591 H0 Z" fill="var(--charcoal)"/>
    <path d="M28,467 C120,485 190,450 250,395 C290,360 330,355 357,362" fill="none" stroke="var(--blue-deep)" stroke-width="6"/>
    <path d="M0,460 C60,478 130,478 182,455 C130,490 60,500 0,485 Z" fill="var(--red)"/>
  </svg>

  <ul class="contact">
    <li class="contact__item">555 390 2176
      <svg class="contact__icon" viewBox="0 0 16 16" aria-hidden="true"><path d="M1,6 C1,2 15,2 15,6 L12,7 L11,5 C9,4.5 7,4.5 5,5 L4,7 Z M4,8 H12 L14,14 H2 Z" fill="var(--white)"/></svg>
    </li>
    <li class="contact__item">info@rbpawstraining.example
      <svg class="contact__icon" viewBox="0 0 16 16" aria-hidden="true"><rect x="1" y="3" width="14" height="10" fill="var(--white)"/><path d="M1,3 L8,9 L15,3 M1,13 L6,8 M15,13 L10,8" fill="none" stroke="var(--charcoal)" stroke-width="1.2"/></svg>
    </li>
    <li class="contact__item">www.rbpawstraining.example
      <svg class="contact__icon" viewBox="0 0 16 16" aria-hidden="true"><circle cx="8" cy="8" r="7" fill="var(--white)"/><path d="M1,8 H15 M8,1 V15 M2.5,4.5 H13.5 M2.5,11.5 H13.5 M8,1 C4,4 4,12 8,15 M8,1 C12,4 12,12 8,15" fill="none" stroke="var(--charcoal)" stroke-width="0.9"/></svg>
    </li>
  </ul>
</section>

</body>
</html>
```